Evacuation Diagram Template

Safe-ROUTA is an Australian business specialising in workplace emergency management.
One of our core services is that of producing ‘Evacuation Diagrams’. These are graphical representations of a buildings floor plan that details information on nearest emergency exits and fire equipment. These are typically displayed in prominent locations throughout the building.
Consistent with our new logo (attached), we would like to overhaul the template that our evacuation diagrams are inserted within. (We do not require the artwork for individual floor plans, but rather a new design of the template our diagrams are published within).
There are a number of restrictions that must be considered to ensure these are compliant with Australian Standards. Information regarding this is attached in the document. Further guidance will be provided once an initial theme is agreed upon.
There is no requirement to copy the existing layouts. We are looking for a fresh idea to revolutionise the graphic appeal of our diagrams.
Minimum
• Evacuation diagram should be in A3 size format.
• The minimum ‘floor plan’ area should be 200 mm x 200 mm
• The maximum siteplan area is 90 mm and should be at 1:1 ratio
• Refer to ‘Design Template.pdf in Portrait format
• Final files to be in .AI format. If possible, in CS6 version. PS is accepted.
Look and feel
Each slider illustrates characteristics of the customer's brand and the style your logo design should communicate.

```html
<!DOCTYPE html>
<html lang="en">
<head>
<meta charset="utf-8">
<title>Safe-ROUTA Evacuation Diagram Template</title>
<link href="https://fonts.googleapis.com/css2?family=Barlow+Condensed:wght@600;700&family=Arimo:wght@400;700&display=swap" rel="stylesheet">
<style>
  :root{
    --navy:#2f4f8a;
    --green:#2ea24f;
    --red:#ea2a2f;
    --white:#ffffff;
    --ink:#222a33;
    --page:#c9d0dc;
    --plan:#eef2f7;
    --map:#b9c6d9;
  }
  *{box-sizing:border-box;margin:0;padding:0}
  html,body{width:1200px;height:1200px;overflow:hidden;background:var(--page);font-family:"Arimo",Arial,sans-serif;color:var(--ink)}
  .sheet{position:absolute;left:20px;top:180px;width:1160px;height:840px;background:var(--white);padding:18px;display:flex;gap:14px}

  .diagram{flex:0 0 800px;background:var(--navy);border-radius:14px;padding:14px;display:flex;flex-direction:column;gap:12px}
  .header{display:flex;align-items:center;gap:28px;height:64px}
  .brand-name{font-family:"Arimo",Arial,sans-serif;font-weight:400;font-size:24px;color:var(--white);white-space:nowrap}
  .title{font-family:"Barlow Condensed",sans-serif;font-weight:700;font-size:50px;letter-spacing:2px;color:var(--white);white-space:nowrap}

  .tab{font-family:"Barlow Condensed",sans-serif;font-weight:600;font-size:26px;letter-spacing:1px;color:var(--white);height:30px;line-height:30px}
  .floorplan{flex:1;background:var(--white);padding:16px;display:flex;flex-direction:column;position:relative}
  .plan-drawing{flex:1;background:var(--plan);border:2px solid var(--ink)}
  .plan-note{position:absolute;right:20px;bottom:2px;font-size:10px;font-style:italic}

  .legend{height:200px;background:var(--white);padding:14px 20px;display:flex;flex-direction:column;justify-content:space-between}
  .legend-items{display:grid;grid-template-columns:repeat(4,1fr);row-gap:14px}
  .legend-item{display:flex;align-items:center;gap:10px;font-size:13px;line-height:1.15}
  .compliance{font-size:11px;text-align:center;line-height:1.5}

  .info{flex:1;background:var(--green);border-radius:14px;padding:14px;display:flex;flex-direction:column;gap:10px}
  .business{color:var(--white);font-size:19px;line-height:1.25;padding:6px 4px 10px}
  .strip{background:var(--navy);color:var(--white);font-family:"Barlow Condensed",sans-serif;font-weight:600;font-size:22px;padding:2px 10px;letter-spacing:1px}
  .race{background:var(--red);color:var(--white);padding:12px 14px;display:flex;flex-direction:column;gap:8px}
  .race-title{font-size:24px;letter-spacing:0.5px;white-space:nowrap}
  .step{display:flex;align-items:center;gap:10px}
  .step-letter{width:32px;height:32px;background:var(--white);color:var(--red);border-radius:4px;display:flex;align-items:center;justify-content:center;font-size:24px;font-weight:700;flex:none}
  .step-text{font-size:11px;line-height:1.3}
  .siteplan{flex:1;background:var(--white);padding:10px;display:flex;flex-direction:column;gap:8px}
  .site-map{flex:1;background:var(--map)}
  .prepared{font-size:10px;line-height:1.5}
</style>
</head>
<body>
<main class="sheet">
  <section class="diagram">
    <header class="header">
      <span class="brand-name">Safe-ROUTA</span>
      <h1 class="title">EVACUATION DIAGRAM</h1>
    </header>

    <div class="tab">FLOORPLAN AREA</div>
    <div class="floorplan">
      <div class="plan-drawing" role="img" aria-label="Building floor plan with exit route, equipment locations and You Are Here marker"></div>
      <span class="plan-note">*floor plan NOT to scale</span>
    </div>

    <div class="tab">LEGEND</div>
    <div class="legend">
      <div class="legend-items">
        <div class="legend-item">
          <svg width="30" height="30" viewBox="0 0 30 30"><rect x="1" y="1" width="28" height="28" fill="#fff" stroke="#e8262b" stroke-width="2"/><rect x="6" y="11" width="18" height="8" rx="2" fill="#e8262b"/></svg>
          <span>DCP<br>Extinguisher</span>
        </div>
        <div class="legend-item">
          <svg width="30" height="30" viewBox="0 0 30 30"><rect x="1" y="1" width="28" height="28" fill="#fff" stroke="#e8262b" stroke-width="2"/><rect x="6" y="11" width="18" height="8" rx="2" fill="#e8262b"/><rect x="14" y="11" width="10" height="8" fill="#222"/></svg>
          <span>CO2<br>Extinguisher</span>
        </div>
        <div class="legend-item">
          <svg width="30" height="30" viewBox="0 0 30 30"><rect width="30" height="30" fill="#2ea24f"/><path d="M12 6h6v6h6v6h-6v6h-6v-6H6v-6h6z" fill="#fff"/></svg>
          <span>First Aid<br>Equipment</span>
        </div>
        <div class="legend-item">
          <svg width="30" height="30" viewBox="0 0 30 30"><rect width="30" height="30" fill="#2ea24f"/><circle cx="15" cy="13" r="6" fill="none" stroke="#fff" stroke-width="2"/><circle cx="15" cy="13" r="2" fill="#fff"/></svg>
          <span>Emergency<br>Eyewash</span>
        </div>
        <div class="legend-item">
          <svg width="30" height="30" viewBox="0 0 30 30"><rect width="30" height="30" fill="#2ea24f"/><path d="M9 6h12M15 6v4" stroke="#fff" stroke-width="2"/><rect x="12" y="13" width="6" height="12" fill="#fff"/></svg>
          <span>Emergency<br>Shower</span>
        </div>
        <div class="legend-item">
          <svg width="30" height="30" viewBox="0 0 30 30"><rect width="30" height="30" fill="#2ea24f"/><text x="15" y="14" font-size="9" font-weight="700" fill="#fff" text-anchor="middle" font-family="Arimo,sans-serif">Spill</text><text x="15" y="24" font-size="9" font-weight="700" fill="#fff" text-anchor="middle" font-family="Arimo,sans-serif">Kit</text></svg>
          <span>Emergency<br>Spill Kit</span>
        </div>
        <div class="legend-item">
          <svg width="30" height="30" viewBox="0 0 30 30"><rect width="30" height="30" fill="#2ea24f"/><rect x="5" y="5" width="20" height="20" fill="none" stroke="#fff" stroke-width="2"/><circle cx="17" cy="10" r="2" fill="#fff"/><path d="M16 13l-3 5 4 2-2 4M13 18l-4-1" stroke="#fff" stroke-width="2" fill="none"/></svg>
          <span>Emergency<br>EXIT</span>
        </div>
        <div class="legend-item">
          <svg width="30" height="30" viewBox="0 0 30 30"><path d="M3 15l8-6v12z" fill="#2ea24f"/><circle cx="17" cy="15" r="3" fill="#2ea24f"/><circle cx="25" cy="15" r="3" fill="#2ea24f"/></svg>
          <span>EXIT<br>Route</span>
        </div>
      </div>
      <p class="compliance">This Evacuation diagram has been issued in compliance with Australian Standard 3745:2010.<br>An annual review of this diagram must be documented to maintain validity.</p>
    </div>
  </section>

  <aside class="info">
    <div class="business">Business Name<br>Business Address Line 1<br>Business Address Line 2<br>Floor Level</div>
    <div class="strip">RACE</div>
    <div class="race">
      <div class="race-title">IN CASE OF FIRE</div>
      <div class="step"><span class="step-letter">R</span><span class="step-text">Remove people from<br>immediate danger</span></div>
      <div class="step"><span class="step-letter">A</span><span class="step-text">Alert others &amp; raise the alarm<br>Contact emergency services '000'</span></div>
      <div class="step"><span class="step-letter">C</span><span class="step-text">Confine fire &amp; smoke<br>Where practical, close doors and windows behind you</span></div>
      <div class="step"><span class="step-letter">E</span><span class="step-text">Evacuate the building<br>Proceed to the nominated assembly area &amp; remain there until instructed</span></div>
    </div>
    <div class="strip">SITEPLAN AREA</div>
    <div class="siteplan">
      <div class="site-map" role="img" aria-label="Site plan showing buildings, street name and assembly area"></div>
      <p class="prepared">Prepared by: Safe-ROUTA | 1300 555 014<br>ISSUED: June 2019 &nbsp;VALIDITY: June 2024</p>
    </div>
  </aside>
</main>
</body>
</html>
```